Prominent Trial Lawyer need a Brochure Design for his firm

Douglas R. Pembry of The Pembry Law Firm has been successfully trying severe and complex for over 28 years. He holds the largest verdict in the history of South Georgia of $150,000,000.00 before the late Gerald T. Voskin in the Harlow District of the Lower District of Marren. He specializes in sever injuries, whether by auto accident, trucking accident or medical malpractice. He is also well know for his successful trial of business disputes and high net-worth Divorces.
Target Market(s)
Persons who need an aggressive, experienced trial lawyer especially for personal injury, but also for other civil and business matters, high end divorde
Industry/Entity Type
Medical
Contact Information for Business Card
Need to use coloring and logo uplaoded
Requirements
Must have
- 1) biography of principal, Douglas R. Pembry
- 2) what we do
- 3) specific cases handled, with specific outcomes (will be supplied)

```html
<!DOCTYPE html>
<html lang="en">
<head>
<meta charset="utf-8">
<title>The Pembry Law Firm — Trifold Brochure</title>
<link href="https://fonts.googleapis.com/css2?family=Cinzel:wght@400;700&family=Roboto:wght@400;500;700&family=Tinos:ital,wght@0,400;1,400;1,700&display=swap" rel="stylesheet">
<style>
  :root {
    --red: #e41f26;
    --red-dark: #b3121a;
    --ink: #2b2b2b;
    --grey-bg: #bdbdbd;
    --panel-white: #ffffff;
    --panel-grey-top: #f4f4f4;
    --panel-grey-bottom: #dcdcdc;
    --logo-grey: #c9c9c9;
  }
  * { box-sizing: border-box; margin: 0; padding: 0; }
  html, body {
    width: 1200px; height: 952px; overflow: hidden;
    background: var(--grey-bg);
    font-family: "Roboto", Arial, sans-serif;
    color: var(--ink);
  }
  .brochure {
    position: absolute; left: 82px; top: 62px;
    width: 1035px; height: 828px;
    display: flex;
    box-shadow: 0 4px 18px rgba(0,0,0,.25);
  }
  .panel { position: relative; width: 345px; height: 100%; overflow: hidden; }

  /* Left panel */
  .panel--bio { background: linear-gradient(#fff, #f1f1f1); }
  .quote-block {
    height: 196px; background: var(--red); color: #fff;
    display: flex; align-items: center; justify-content: center;
    padding: 0 22px 20px;
    font-family: "Tinos", "Times New Roman", serif;
    font-style: italic; font-weight: 700; font-size: 19.5px; line-height: 1.2;
    text-align: center;
  }
  .team-photo {
    height: 258px;
    background: linear-gradient(135deg, #8a8177 0%, #5d5650 45%, #2f3346 75%, #4a4a52 100%);
  }
  .bio { padding: 26px 28px 0 28px; }
  .bio__name { color: var(--red); font-weight: 500; font-size: 22px; line-height: 1.1; }
  .bio__role {
    font-family: "Tinos", "Times New Roman", serif; font-style: italic;
    font-size: 17px; color: #333; margin: 2px 0 10px;
  }
  .bio__text { font-size: 14.2px; line-height: 1.27; text-align: justify; color: #222; }

  /* Middle panel */
  .panel--practice { background: var(--panel-white); }
  .ribbon { position: relative; margin: 42px auto 0; width: 312px; height: 56px; }
  .ribbon svg { position: absolute; inset: 0; }
  .ribbon__label {
    position: absolute; left: 0; right: 0; top: 9px;
    text-align: center; color: #fff; font-size: 20px; font-weight: 500;
  }
  .practice__intro { padding: 22px 22px 0 22px; font-size: 14.2px; line-height: 1.27; text-align: justify; }
  .practice__intro p + p { margin-top: 8px; }
  .firm-name {
    margin: 50px auto 0; width: 200px; text-align: center;
    display: flex; flex-direction: column; align-items: center; gap: 12px;
    font-family: "Cinzel", Georgia, serif; font-size: 20px; color: var(--logo-grey); line-height: 1.25;
  }
  .firm-name__dot { width: 62px; height: 62px; border-radius: 50%; background: #e6e6e6; }
  .specialties { position: absolute; left: 40px; right: 14px; top: 512px; }
  .specialties__title {
    font-family: "Tinos", "Times New Roman", serif; font-style: italic; font-weight: 700;
    color: var(--red); font-size: 20px; text-align: center; margin-bottom: 8px; margin-left: -20px;
  }
  .specialties__list { list-style: none; }
  .specialties__item {
    display: flex; align-items: flex-start; gap: 9px;
    font-family: "Cinzel", Georgia, serif; font-size: 15.5px; letter-spacing: .6px;
    line-height: 1.15; margin-bottom: 8px; color: #222;
  }
  .specialties__item svg { flex: none; margin-top: 2px; }

  /* Contact band */
  .contact-band {
    position: absolute; left: 0; bottom: 0; width: 690px; height: 94px;
    background: var(--red); color: #fff;
    display: flex; align-items: center; justify-content: center;
    font-size: 20.5px; letter-spacing: .2px; z-index: 2; padding-bottom: 8px;
  }

  /* Right panel */
  .panel--cases { background: linear-gradient(var(--panel-grey-top), var(--panel-grey-bottom)); }
  .gavel-photo {
    height: 250px;
    background: radial-gradient(ellipse at 30% 45%, #a8653a 0%, #6e3a1e 35%, #b8b2a6 65%, #e9e4dc 100%);
  }
  .cases__heading {
    margin-top: 28px; text-align: center;
    font-family: "Cinzel", Georgia, serif; font-size: 18px; line-height: 1.3; color: #222;
  }
  .cases__heading .accent { color: var(--red); }
  .cases__body { padding: 22px 26px 0 22px; }
  .cases__body p { font-size: 14.2px; line-height: 1.27; text-align: justify; color: #333; margin-bottom: 18px; }
</style>
</head>
<body>
<main class="brochure">
  <section class="panel panel--bio">
    <blockquote class="quote-block">“Whether you are against Insurance Companies, Fortune 500 Companies or Goverments, we level the field and give you the edge.”</blockquote>
    <div class="team-photo" role="img" aria-label="Group photo of the firm's attorneys in business attire"></div>
    <div class="bio">
      <h2 class="bio__name">Douglas Pembry</h2>
      <p class="bio__role">- the Mind behind Pembry Law Firm</p>
      <p class="bio__text">Douglas graduated with honors from the University of Marren School of Law in 1986. He also received his BBA from UM in 1982. Douglas founded the Pembry Law Firm in 1989 and has spent the last 26 years trying complex cases, including medical malpractice, personal injury, criminal and civil cases. He holds the largest verdict in the Lower District of Marren of $150,000,000.00. Currently he specializes in severe personal injury cases and commercial litigation.</p>
    </div>
  </section>

  <section class="panel panel--practice">
    <div class="ribbon">
      <svg width="312" height="56" viewBox="0 0 312 56">
        <polygon points="0,14 36,14 36,54 0,54 12,34" fill="var(--red)"/>
        <polygon points="312,14 276,14 276,54 312,54 300,34" fill="var(--red)"/>
        <polygon points="36,46 36,54 46,46" fill="var(--red-dark)"/>
        <polygon points="276,46 276,54 266,46" fill="var(--red-dark)"/>
        <rect x="36" y="0" width="240" height="46" fill="var(--red)"/>
      </svg>
      <span class="ribbon__label">Areas of Practice</span>
    </div>
    <div class="practice__intro">
      <p>We love the practice of law and how it can help to resolve your civil and family disputes, to right the wrongs done by others, to protect your constitutional rights if you happened to be accused of a crime, to seek fair monetary compensation if you are entitled to.</p>
      <p>We at The Pembry Law Firm can ensure that you are best represented in courts utilizing the most up-to-date laws, diligent preparation and insightful understanding of your matter.</p>
    </div>
    <div class="firm-name">
      <span class="firm-name__dot"></span>
      <span>The Pembry Law Firm</span>
    </div>
    <div class="specialties">
      <h3 class="specialties__title">We have specilized in:</h3>
      <ul class="specialties__list">
        <li class="specialties__item"><svg width="12" height="12" viewBox="0 0 12 12"><circle cx="6" cy="6" r="6" fill="var(--red)"/><path d="M3.2 6.2l2 2 3.6-4" stroke="#fff" stroke-width="1.6" fill="none"/></svg>Business Litigation</li>
        <li class="specialties__item"><svg width="12" height="12" viewBox="0 0 12 12"><circle cx="6" cy="6" r="6" fill="var(--red)"/><path d="M3.2 6.2l2 2 3.6-4" stroke="#fff" stroke-width="1.6" fill="none"/></svg>General Civil Litigation</li>
        <li class="specialties__item"><svg width="12" height="12" viewBox="0 0 12 12"><circle cx="6" cy="6" r="6" fill="var(--red)"/><path d="M3.2 6.2l2 2 3.6-4" stroke="#fff" stroke-width="1.6" fill="none"/></svg>Personal Injury</li>
        <li class="specialties__item"><svg width="12" height="12" viewBox="0 0 12 12"><circle cx="6" cy="6" r="6" fill="var(--red)"/><path d="M3.2 6.2l2 2 3.6-4" stroke="#fff" stroke-width="1.6" fill="none"/></svg>Criminal Defense</li>
        <li class="specialties__item"><svg width="12" height="12" viewBox="0 0 12 12"><circle cx="6" cy="6" r="6" fill="var(--red)"/><path d="M3.2 6.2l2 2 3.6-4" stroke="#fff" stroke-width="1.6" fill="none"/></svg>Family Law</li>
        <li class="specialties__item"><svg width="12" height="12" viewBox="0 0 12 12"><circle cx="6" cy="6" r="6" fill="var(--red)"/><path d="M3.2 6.2l2 2 3.6-4" stroke="#fff" stroke-width="1.6" fill="none"/></svg>Real Estate Transaction &amp; Litigation</li>
      </ul>
    </div>
  </section>

  <section class="panel panel--cases">
    <div class="gavel-photo" role="img" aria-label="Close-up photo of a wooden judge's gavel resting beside an open law book"></div>
    <h2 class="cases__heading"><span class="accent">Prominent</span> Cases<br>of<br>The Pembry Law Firm</h2>
    <div class="cases__body">
      <p>Lorem Ipsum. Proin gravida nibh vel velit auctor aliquet. Aenean sollicitudin, lorem quis bibendum auctor, nisi elit consequat ipsum, nec sagittis sem nibh id elit. Duis sed odio sit amet nibh vulputate cursus a sit amet mauris.</p>
      <p>Lorem Ipsum. Proin gravida nibh vel velit auctor aliquet. Aenean sollicitudin, lorem quis bibendum auctor, nisi elit consequat ipsum, nec sagittis sem nibh id elit. Duis sed odio sit amet nibh vulputate cursus a sit amet mauris.</p>
      <p>Lorem Ipsum. Proin gravida nibh vel velit auctor aliquet. Aenean sollicitudin, lorem quis bibendum auctor, nisi elit consequat ipsum, nec sagittis sem nibh id elit. Duis sed odio sit amet nibh vulputate cursus a sit amet mauris. Duis sed odio sit amet nibh vulputate cursus a sit amet mauris.</p>
    </div>
  </section>

  <footer class="contact-band">We're Always Here to Help. You May Call Us at (555) 014.2760</footer>
</main>
</body>
</html>
```